Flyer Design for Norvane LLC

We need a Flyer for a new company called “Norvane LLC”. This is a technology process improvement company providing a comprehensive assessment of the technology used to run their business. The documentation and review process delivers the visibility and reassurance they need to protect their business and plan for the future. The product is called “Systems Charterwork”. Our primary target is small-medium size businesses, with the deliverables going to the decision maker.

We would like to see the designs use the color blue. Our tag line is "Protect Your Business · Take Control of IT".

- Attached: Norvane LLC Overview document we put together as a starting point. Use as much or as little as you wish.
- Attached: Business Card and Logo designs for colors, etc.

Industry/Entity Type

It Company

```html
<!DOCTYPE html>
<html lang="en">
<head>
<meta charset="utf-8">
<title>Norvane LLC – Protect Your Business</title>
<link rel="stylesheet" href="https://fonts.googleapis.com/css2?family=Exo+2:wght@600;700&family=Questrial&family=Crimson+Text&display=swap">
<style>
  :root {
    --brand-blue: #0f6cbf;
    --pie-blue: #2f6fc6;
    --ring-blue: #a7c0e6;
    --panel-gray: #848587;
    --photo-tone-a: #c9c4bd;
    --photo-tone-b: #7f8a96;
    --paper: #ffffff;
    --ink-light: #ffffff;
    --head-font: "Exo 2", sans-serif;
    --body-font: "Questrial", sans-serif;
    --chart-font: "Crimson Text", serif;
  }
  html, body { margin: 0; padding: 0; overflow: hidden; }
  body { width: 1041px; height: 1200px; background: var(--paper); }
  .flyer { position: relative; width: 1041px; height: 1200px; overflow: hidden; background: var(--paper); color: var(--ink-light); font-family: var(--body-font); }
  .backdrop { position: absolute; inset: 0; width: 100%; height: 100%; }
  .abs { position: absolute; margin: 0; }

  .headline { left: 116px; top: 40px; font-family: var(--head-font); font-weight: 700; font-size: 66px; line-height: 66px; letter-spacing: 1px; }
  .tagline { left: 118px; top: 264px; font-family: var(--head-font); font-weight: 600; font-size: 24px; letter-spacing: .5px; }

  .brand-name { left: 748px; top: 128px; width: 264px; text-align: center; font-family: var(--head-font); font-weight: 700; font-size: 30px; color: var(--brand-blue); letter-spacing: 1px; }
  .brand-mark { left: 862px; top: 58px; width: 46px; height: 46px; border-radius: 50%; background: var(--brand-blue); }

  .intro-title { left: 31px; top: 454px; font-family: var(--head-font); font-weight: 700; font-size: 27px; line-height: 33px; }
  .intro-text { left: 31px; top: 540px; width: 270px; font-size: 14.5px; line-height: 24.5px; }

  .section-title { font-family: var(--head-font); font-weight: 700; font-size: 22px; padding-bottom: 4px; border-bottom: 2px solid var(--ink-light); }
  .help-title { left: 31px; top: 675px; width: 250px; }
  .help-text { left: 31px; top: 726px; width: 392px; font-size: 14px; line-height: 24.6px; text-align: justify; }
  .deliver-title { left: 31px; top: 987px; width: 370px; }

  .deliverables { top: 1036px; list-style: none; padding: 0; font-size: 15px; line-height: 18px; }
  .deliverables li { position: relative; padding-left: 24px; margin-bottom: 7px; }
  .deliverables li::before { content: ""; position: absolute; left: 0; top: 2px; width: 10px; height: 10px; border: 2px solid var(--ink-light); border-radius: 50%; }
  .col-one { left: 31px; width: 200px; }
  .col-two { left: 252px; width: 200px; }

  .areas-chart { left: 472px; top: 643px; width: 300px; height: 300px; }
  .areas-caption { left: 522px; top: 950px; width: 200px; text-align: center; font-family: var(--head-font); font-weight: 700; font-size: 18px; line-height: 26px; }

  .contact-title { left: 700px; top: 1022px; width: 301px; text-align: right; font-family: var(--head-font); font-weight: 700; font-size: 28px; padding-bottom: 6px; border-bottom: 2px solid var(--ink-light); }
  .contact-list { left: 640px; top: 1080px; width: 360px; list-style: none; padding: 0; text-align: right; }
  .contact-list li { display: flex; justify-content: flex-end; align-items: center; gap: 16px; height: 34px; font-size: 22px; }
  .contact-list .phone { font-size: 31px; font-family: var(--body-font); height: 40px; }
  .contact-list svg { width: 20px; height: 20px; flex: none; }
</style>
</head>
<body>
<main class="flyer">
  <svg class="backdrop" viewBox="0 0 837 1080" preserveAspectRatio="none" aria-hidden="false">
    <defs>
      <linearGradient id="meetingTone" x1="0" y1="0" x2="1" y2="1">
        <stop offset="0" stop-color="var(--photo-tone-a)"/>
        <stop offset="1" stop-color="var(--photo-tone-b)"/>
      </linearGradient>
    </defs>
    <polygon class="panel-blue-top" points="0,0 423,0 548,119 238,414 0,184" fill="var(--brand-blue)"/>
    <polygon class="panel-gray" points="0,184 238,414 648,819 388,1080 0,1080" fill="var(--panel-gray)"/>
    <polygon class="meeting-photo" role="img" aria-label="Photo of a business team meeting around a conference table in a bright office" points="238,414 548,114 837,404 837,644 648,819" fill="url(#meetingTone)"/>
    <polygon class="panel-blue-bottom" points="388,1080 837,644 837,1080" fill="var(--brand-blue)"/>
  </svg>

  <h1 class="abs headline">PROTECT<br>YOUR<br>BUSINESS</h1>
  <p class="abs tagline">TAKE CONTROL OF IT</p>

  <span class="abs brand-mark" aria-hidden="true"></span>
  <p class="abs brand-name">NORVANE LLC</p>

  <h2 class="abs intro-title">You have big<br>plans, right?</h2>
  <p class="abs intro-text">Technology may help you get there, but how can you plan where you want to go without defining where you are today?</p>

  <h2 class="abs section-title help-title">WE CAN HELP!</h2>
  <p class="abs help-text">Norvane LLC provides a comprehensive assessment of the technology used to run your business. The documentation and review process delivers the visibility and reassurance you need to protect your business. Our team understands that each business operates on its own unique complexities, and crafting a solution requires a custom, unbiased review. Positioning your company with the right insight is intrumental to your success and our goal as your technology partner.</p>

  <h2 class="abs section-title deliver-title">DOSSIER DELIVERABLES</h2>
  <ul class="abs deliverables col-one">
    <li>Executive Dashboard</li>
    <li>Technology Product Summary</li>
    <li>Recommended IT Policies</li>
    <li>Potential Cost Savings</li>
  </ul>
  <ul class="abs deliverables col-two">
    <li>Technology Recommendations</li>
    <li>In-depth Questionnaire</li>
    <li>Technology Product Details</li>
    <li>Full Infrastructure Detailed Report</li>
  </ul>

  <svg class="abs areas-chart" viewBox="-150 -150 300 300" role="img" aria-label="Five functional areas cycle">
    <circle r="148" fill="var(--paper)"/>
    <circle r="140" fill="var(--ring-blue)"/>
    <circle r="118" fill="var(--pie-blue)"/>
    <g stroke="var(--paper)" stroke-width="4">
      <line x1="0" y1="0" x2="0" y2="-140"/>
      <line x1="0" y1="0" x2="133" y2="-43"/>
      <line x1="0" y1="0" x2="82" y2="113"/>
      <line x1="0" y1="0" x2="-82" y2="113"/>
      <line x1="0" y1="0" x2="-133" y2="-43"/>
    </g>
    <g fill="var(--paper)">
      <polygon points="-4,-140 10,-128 -4,-118"/>
      <polygon points="127,-52 136,-34 118,-36"/>
      <polygon points="86,104 72,118 68,104"/>
      <polygon points="-74,118 -90,110 -78,100"/>
      <polygon points="-134,-32 -128,-50 -116,-38"/>
    </g>
    <g fill="var(--ink-light)" font-family="var(--chart-font)" font-size="12" text-anchor="middle">
      <text x="-52" y="-72">IT</text>
      <text x="-52" y="-58">Administration</text>
      <text x="52" y="-72">IT Service</text>
      <text x="52" y="-58">Delivery</text>
      <text x="80" y="22">Infrastructure</text>
      <text x="80" y="36">Services</text>
      <text x="0" y="84">Application</text>
      <text x="0" y="98">Services</text>
      <text x="-78" y="30">IT Planning</text>
    </g>
  </svg>
  <p class="abs areas-caption">Evaluating Five<br>Functional Areas</p>

  <h2 class="abs contact-title">CONTACT US</h2>
  <ul class="abs contact-list">
    <li class="phone">866-555-0142
      <svg viewBox="0 0 20 20" aria-hidden="true"><path d="M3 8c0-3 3-5 7-5s7 2 7 5l-3 1-1-2H7L6 9z M5 11h10l1 6H4z" fill="var(--ink-light)"/></svg>
    </li>
    <li>sales@norvanellc.com
      <svg viewBox="0 0 20 20" aria-hidden="true"><rect x="2" y="4" width="16" height="12" fill="var(--ink-light)"/><path d="M2 4l8 7 8-7" fill="none" stroke="var(--brand-blue)" stroke-width="1.5"/></svg>
    </li>
    <li>www.norvanellc.com
      <svg viewBox="0 0 20 20" aria-hidden="true"><g fill="none" stroke="var(--ink-light)" stroke-width="1.6"><circle cx="10" cy="10" r="7.5"/><ellipse cx="10" cy="10" rx="3.5" ry="7.5"/><line x1="2.5" y1="10" x2="17.5" y2="10"/><line x1="10" y1="2.5" x2="10" y2="17.5"/></g></svg>
    </li>
  </ul>
</main>
</body>
</html>
```